We're launching a new live touring show called "Hollow Lanterns, Quiet Echoes and Method - A LIVE THEATRE EVENING" and we're looking to create a show poster. The itself will be a combination of mentalism tricks that are explainable done by one expert/magician and another expert who is well studied in the science of mind reading, telepathy, telekinesis, etc. The audience will be left entertained and learning that there are some things in science that are still yet to be explained. We'd like the poster to have it clear that it's a live show with 2 experts (man and a woman) and we want it to feel like a mix of academic and entertainment value. Not too mystical. No crystal balls or anything.

```html
<!DOCTYPE html>
<html lang="en">
<head>
<meta charset="utf-8">
<title>Hollow Lanterns, Quiet Echoes and Method – Show Poster</title>
<link href="https://fonts.googleapis.com/css2?family=Bebas+Neue&family=Montserrat:wght@400;700&family=Oswald:wght@300;600&display=swap" rel="stylesheet">
<style>
  :root {
    --page-bg: #ebe7fb;
    --poster-deep: #1c1840;
    --poster-purple: #3a2466;
    --poster-violet: #6a2fa0;
    --green-top: #056a37;
    --green-bottom: #6cb546;
    --ink-white: #ffffff;
    --ink-navy: #231a5a;
    --badge-fill: rgba(22, 22, 52, 0.78);
  }
  * { margin: 0; padding: 0; box-sizing: border-box; }
  html, body {
    width: 1200px; height: 1200px; overflow: hidden;
    background: var(--page-bg);
  }
  .poster {
    position: absolute; left: 238px; top: 91px;
    width: 724px; height: 1018px;
    overflow: hidden;
    box-shadow: 0 6px 22px rgba(40, 30, 80, 0.35);
    background:
      radial-gradient(ellipse 160px 120px at 0 0, var(--poster-violet), transparent 70%),
      radial-gradient(ellipse 160px 120px at 100% 0, var(--poster-violet), transparent 70%),
      radial-gradient(ellipse 420px 300px at 50% 0, #15142e, transparent 80%),
      linear-gradient(180deg, #2b1f55 0%, var(--poster-purple) 45%, #2a1d54 75%, var(--poster-purple) 88%, var(--poster-deep) 100%);
  }
  .doodle-layer {
    position: absolute; inset: 0;
    background: radial-gradient(ellipse at 50% 60%, rgba(120, 90, 170, 0.10), transparent 70%);
  }
  .hex-panel { position: absolute; left: 0; top: 0; width: 724px; height: 1018px; }
  .title {
    position: absolute; left: 0; width: 724px; top: 176px;
    text-align: center; color: var(--ink-white);
    font-family: "Bebas Neue", sans-serif; font-weight: 400;
    font-size: 74px; line-height: 90px; letter-spacing: 0.07em;
    padding-left: 0.07em;
    white-space: nowrap;
  }
  .rule {
    position: absolute; height: 1.5px;
    background: linear-gradient(90deg, transparent, rgba(255,255,255,0.85) 50%, transparent);
  }
  .rule--upper { left: 130px; width: 464px; top: 454px; }
  .rule--lower { left: 130px; width: 464px; top: 507px; }
  .rule--footer { left: 170px; width: 384px; top: 932px; }
  .subtitle {
    position: absolute; left: 0; width: 724px; top: 457px;
    text-align: center; color: var(--ink-navy);
    font-family: "Montserrat", sans-serif; font-weight: 700;
    font-size: 38px; line-height: 46px; letter-spacing: 0.01em;
  }
  .experts {
    position: absolute; left: 0; width: 724px; top: 526px;
    text-align: center; color: var(--ink-white);
    font-family: "Montserrat", sans-serif; font-weight: 400;
    font-size: 29px; line-height: 47px;
  }
  .date-badge {
    position: absolute; left: 263px; top: 647px;
    width: 198px; height: 198px; border-radius: 50%;
    background: var(--badge-fill);
    border: 1.5px solid rgba(255,255,255,0.6);
    text-align: center; color: var(--ink-white);
    font-family: "Oswald", sans-serif;
    padding-top: 30px;
  }
  .date-badge__day { font-weight: 600; font-size: 38px; line-height: 46px; letter-spacing: -0.01em; }
  .date-badge__date { font-weight: 300; font-size: 38px; line-height: 48px; }
  .showtime {
    position: absolute; left: 0; width: 724px; top: 872px;
    text-align: center; color: var(--ink-white);
    font-family: "Montserrat", sans-serif; font-weight: 700; font-size: 35px; line-height: 44px;
  }
  .venue {
    position: absolute; left: 0; width: 724px; top: 953px;
    text-align: center; color: var(--ink-white);
    font-family: "Montserrat", sans-serif; font-weight: 400; font-size: 24px; line-height: 30px;
  }
</style>
</head>
<body>
  <main class="poster">
    <div class="doodle-layer" role="img" aria-label="Faint hand-drawn science doodles: formulas, flasks, atoms and clocks"></div>

    <svg class="hex-panel" viewBox="0 0 724 1018" aria-hidden="true">
      <defs>
        <linearGradient id="hexGreen" x1="0" y1="0" x2="0" y2="1">
          <stop offset="0" stop-color="#056a37"/>
          <stop offset="1" stop-color="#6cb546"/>
        </linearGradient>
      </defs>
      <path d="M 322 46 Q 362 22 402 46
               L 646 190 Q 686 214 686 260
               L 686 550 Q 686 596 646 620
               L 362 780
               L 78 620 Q 38 596 38 550
               L 38 260 Q 38 214 78 190 Z"
            fill="url(#hexGreen)" stroke="#ffffff" stroke-width="1"/>
    </svg>

    <h1 class="title">Hollow Lanterns,<br>Quiet Echoes<br>and Method</h1>

    <div class="rule rule--upper"></div>
    <p class="subtitle">A LIVE THEATRE EVENING</p>
    <div class="rule rule--lower"></div>

    <p class="experts">Live show with 2 experts<br>(man and a woman)</p>

    <div class="date-badge">
      <div class="date-badge__day">SATURDAY,</div>
      <div class="date-badge__date">JANUARY 24</div>
      <div class="date-badge__date">2025</div>
    </div>

    <p class="showtime">5:00–7:00 PM</p>
    <div class="rule rule--footer"></div>
    <p class="venue">Location Name, Location Address</p>
  </main>
</body>
</html>
```